Site Update/Merger: Darvik Systems

We want to take some content (not ALL the content, but only what is specified) from two or our sites and combine into one
The New Website is in Wordpress too.
The new site needs to be a nice merge between these sites:
◦ https://tovaro-works.example/
◦ https://helmstrand-plan.example/
Theme/topic: this is an Engineering site
The blog must be included on the home page (maybe smaller), and also on the Systems Engineering page (maybe a little bigger, allow the user to browse through all blogs)
Instructions and visual aids:
Step 1: SEE BRIEFING IN THE PDF ATTACHED
Step 2: some pictures for your reference (referenced in the PDF)
Updates
The design of the children pages are not ready, and the designer still needs to load everything into my wordpress site.
Look and feel
Each slider illustrates characteristics of the customer's brand and the style your logo design should communicate.

```html
<!DOCTYPE html>
<html lang="en">
<head>
<meta charset="utf-8">
<title>Darvik Systems — Engineering Services</title>
<link href="https://fonts.googleapis.com/css2?family=Oswald:wght@300;400;500&family=Poppins:wght@400;500;600&display=swap" rel="stylesheet">
<style>
:root{
  --red:#c1272d;
  --ink:#2a2a2e;
  --body:#4a4a4f;
  --muted:#6a6a70;
  --card:#f1f1f3;
  --dark:#2e2c33;
  --line:#e2e2e5;
  --white:#ffffff;
  --deco:#8e8e93;
}
*{box-sizing:border-box;margin:0;padding:0}
html,body{width:1200px;height:2972px;overflow:hidden;background:var(--white)}
body{position:relative;font-family:'Poppins',sans-serif;color:var(--body)}
.abs{position:absolute}
.display{font-family:'Oswald',sans-serif;font-weight:400;color:var(--ink);text-transform:uppercase;letter-spacing:-0.5px}
.ghost{font-family:'Oswald',sans-serif;font-weight:300;text-transform:uppercase;color:transparent;-webkit-text-stroke:1px #d9d9dd;line-height:1}
.rule{height:3px;background:var(--red)}
/* header */
.brand{left:89px;top:28px;display:flex;align-items:center;gap:10px;font-family:'Poppins',sans-serif;font-weight:600;font-size:19px;color:var(--ink);letter-spacing:1px;text-transform:uppercase}
.brand .mark{width:18px;height:18px;background:var(--red)}
.nav{top:34px;font-size:15px;font-weight:500;color:var(--ink);text-transform:uppercase;letter-spacing:.3px}
.nav.active{color:var(--red)}
.nav.active::before{content:"";position:absolute;left:0;right:0;top:-34px;height:3px;background:var(--red)}
/* hero */
.hero-photo{left:530px;top:58px;width:670px;height:465px;background:linear-gradient(90deg,#ffffff 0%,#f4ece6 18%,#e9a37a 50%,#d6652f 75%,#b6522a 100%)}
.thumb-frame{left:854px;top:367px;width:346px;height:156px;background:var(--white)}
.thumb{top:378px;width:153px;height:145px;background:linear-gradient(160deg,#8d9096,#c9c6bd 55%,#6f7075)}
.hero-lead{left:89px;top:325px;width:540px;font-size:16.5px;line-height:25px;color:var(--body)}
.deco-triangle{left:0;top:444px;width:112px;height:232px;background:var(--deco);clip-path:polygon(0 0,100% 50%,0 100%)}
.deco-hatch{left:1030px;top:1408px;width:170px;height:170px;background:var(--deco);clip-path:polygon(47% 0,100% 0,100% 100%,0 100%,0 41%,47% 41%)}
/* cards */
.card{top:599px;width:329px;height:330px;background:var(--card);text-align:center}
.card svg{margin-top:32px}
.card h3{font-family:'Oswald',sans-serif;font-weight:400;font-size:20px;line-height:23px;color:var(--ink);text-transform:uppercase;margin:20px auto 0;width:220px}
.card p{font-size:15px;line-height:20px;margin:12px auto 0;width:240px}
.card .go{display:block;margin:20px auto 0}
/* what we do */
.band{left:0;top:1042px;width:733px;height:425px;background:var(--red);background-image:radial-gradient(rgba(255,255,255,.07) 1px,transparent 1px);background-size:6px 6px}
.band-photo{left:733px;top:992px;width:380px;height:524px;background:linear-gradient(170deg,#6d7078,#a9a9a6 40%,#c8c2b3 60%,#4a5068)}
.band .ghost{-webkit-text-stroke:1px rgba(255,255,255,.35)}
.band p{color:var(--white);font-size:16.5px;line-height:25px}
/* services */
.svc-intro{left:466px;top:1622px;width:420px;font-size:16px;line-height:25px}
.svc-head{font-family:'Oswald',sans-serif;font-weight:400;font-size:24px;color:var(--ink);text-transform:uppercase;letter-spacing:-.3px}
.item-title{font-family:'Oswald',sans-serif;font-size:17px;color:var(--ink);text-transform:uppercase}
.item-text{font-size:15px;line-height:20px;width:300px;margin-top:4px}
.sep{left:181px;width:365px;height:1px;background:var(--line)}
.post{left:658px;width:453px;height:164px;background:var(--white);box-shadow:0 6px 22px rgba(0,0,0,.07)}
.post .pic{position:absolute;left:0;top:0;width:164px;height:164px}
.post .txt{position:absolute;left:184px;top:22px;width:252px}
.post .meta{font-size:12px;color:var(--muted)}
.post h4{font-family:'Oswald',sans-serif;font-weight:400;font-size:16.5px;line-height:21px;color:var(--ink);text-transform:uppercase;margin-top:8px;letter-spacing:-.2px}
.post p{font-size:13.5px;line-height:19px;margin-top:10px}
.view-all{left:658px;top:2339px;font-size:15px;font-weight:600;color:var(--ink);border-bottom:2px solid var(--ink);letter-spacing:.3px}
/* footer */
.footer{left:0;top:2458px;width:1200px;height:514px;background:var(--dark)}
.field{left:264px;top:2634px;width:540px;height:49px;background:var(--white);display:flex;align-items:center;padding-left:24px;gap:12px;font-size:14.5px;color:#666}
.subscribe{left:804px;top:2634px;width:132px;height:49px;background:var(--red);color:var(--white);font-weight:600;font-size:14.5px;display:flex;align-items:center;justify-content:center;letter-spacing:.4px}
.f-brand{left:148px;top:2815px;display:flex;align-items:center;gap:12px;font-weight:600;font-size:26px;color:var(--white);letter-spacing:1.5px;text-transform:uppercase}
.f-brand .mark{width:24px;height:24px;background:var(--red)}
.f-icon{width:42px;height:42px;background:#45434a;display:flex;align-items:center;justify-content:center}
.f-label{font-family:'Oswald',sans-serif;font-size:20px;color:var(--white);text-transform:uppercase}
.f-text{font-size:15px;color:#d8d8dc;margin-top:2px}
.f-rule{left:89px;top:2913px;width:1022px;height:1px;background:#48464d}
.copy{left:0;top:2931px;width:1200px;text-align:center;font-family:'Oswald',sans-serif;font-size:16px;color:var(--white);text-transform:uppercase}
.top-btn{left:1131px;top:2890px;width:46px;height:46px;border-radius:50%;background:var(--white);display:flex;align-items:center;justify-content:center}
</style>
</head>
<body>

<!-- Header -->
<div class="abs brand"><span class="mark"></span>Darvik Systems</div>
<div class="abs nav active" style="left:804px">Home</div>
<div class="abs nav" style="left:894px">Services <svg width="8" height="6" viewBox="0 0 8 6"><path d="M1 1l3 3 3-3" fill="none" stroke="#2a2a2e" stroke-width="1.4"/></svg></div>
<div class="abs nav" style="left:1012px">Contact Us</div>

<!-- Hero -->
<div class="abs hero-photo" role="img" aria-label="Electric vehicle charging cable plugged into an orange car"></div>
<div class="abs thumb-frame"></div>
<div class="abs thumb" style="left:869px" role="img" aria-label="Engineer working on a test rig"></div>
<div class="abs thumb" style="left:1034px" role="img" aria-label="Team reviewing a hardware bench setup"></div>

<div class="abs ghost" style="left:87px;top:152px;font-size:116px">Solutions</div>
<h1 class="abs display" style="left:89px;top:202px;font-size:84px;line-height:1">Who We Are</h1>
<div class="abs rule" style="left:89px;top:307px;width:65px"></div>
<p class="abs hero-lead">A Multi-Disciplinary Consulting and<br>Engineering Service Provider for EV and Other Industries,<br>with a Focus on Systematic Product Development</p>

<div class="abs deco-triangle" role="img" aria-label="Decorative striped triangle pattern"></div>

<!-- Service cards -->
<div class="abs card" style="left:262px">
  <svg width="120" height="110" viewBox="0 0 120 110">
    <g fill="none" stroke="#333" stroke-width="2">
      <circle cx="68" cy="50" r="22"/><path d="M60 72v12h16V72"/><path d="M62 88h12M64 92h8"/>
      <circle cx="32" cy="62" r="14"/><circle cx="32" cy="62" r="5"/>
      <path d="M68 20v-10M92 30l7-7M44 30l-7-7M98 52h10M90 62l12 8M94 40h12"/>
    </g>
    <circle cx="68" cy="50" r="10" fill="#c1272d"/>
  </svg>
  <h3>Systems Engineering Solutions</h3>
  <p>Our Focus: Collaboration, Accountability and Feedback</p>
  <svg class="go" width="18" height="10" viewBox="0 0 18 10"><path d="M0 5h16M12 1l4 4-4 4" fill="none" stroke="#333" stroke-width="1.4"/></svg>
</div>
<div class="abs card" style="left:609px">
  <svg width="120" height="110" viewBox="0 0 120 110">
    <g fill="none" stroke="#333" stroke-width="2">
      <rect x="22" y="38" width="76" height="50" rx="3"/>
      <path d="M40 38V18M52 38V12M60 38V8M68 38V12M80 38V18M40 50l10 10M80 50l-10 10M60 46v28M46 76l8-8M74 76l-8-8"/>
      <circle cx="40" cy="16" r="3"/><circle cx="52" cy="10" r="3"/><circle cx="68" cy="10" r="3"/><circle cx="80" cy="16" r="3"/>
    </g>
    <rect x="10" y="88" width="100" height="10" rx="3" fill="#c1272d"/>
  </svg>
  <h3>Modeling and Hardware in the Loop Consulting</h3>
  <p>From data-driven system identification to real-time...</p>
  <svg class="go" width="18" height="10" viewBox="0 0 18 10"><path d="M0 5h16M12 1l4 4-4 4" fill="none" stroke="#333" stroke-width="1.4"/></svg>
</div>

<!-- What we do -->
<div class="abs band">
  <div class="abs ghost" style="left:87px;top:50px;font-size:112px">Control</div>
  <h2 class="abs display" style="left:89px;top:138px;font-size:58px;line-height:1;color:#fff">What We Do</h2>
  <div class="abs rule" style="left:89px;top:208px;width:48px;background:#fff"></div>
  <p class="abs" style="left:89px;top:228px;width:480px">A team of automotive, control and mechanical engineers from different industries and backgrounds and with more than 10 years of experience that came together to provide cost effective and specialized services to your organization or team in the pursue of your projects goals.</p>
</div>
<div class="abs band-photo" role="img" aria-label="Engineer assembling a large mechanical test fixture"></div>
<div class="abs deco-hatch" role="img" aria-label="Decorative diagonal hatched pattern"></div>

<!-- Our services -->
<h2 class="abs display" style="left:89px;top:1636px;font-size:58px;line-height:1">Our Services</h2>
<div class="abs rule" style="left:97px;top:1709px;width:47px"></div>
<div class="abs" style="left:415px;top:1621px;width:2px;height:98px;background:var(--line)"></div>
<p class="abs svc-intro">This is just a glance at the activities and projects we can contribute to. For more details, go to our services menu or contact us to have a exploratory conversation.</p>

<div class="abs svc-head" style="left:89px;top:1766px">Systems Engineering Solutions</div>
<div class="abs" style="left:89px;top:1809px;font-size:15px">Our Focus: Collaboration, Accountability and Feedback</div>

<svg class="abs" style="left:89px;top:1856px" width="72" height="68" viewBox="0 0 72 68" fill="none" stroke="#c1272d" stroke-width="2">
  <rect x="24" y="2" width="24" height="18" rx="2"/><circle cx="36" cy="9" r="3"/>
  <rect x="2" y="38" width="24" height="18" rx="2"/><circle cx="14" cy="45" r="3"/>
  <rect x="46" y="38" width="24" height="18" rx="2"/><circle cx="58" cy="45" r="3"/>
  <path d="M10 34a28 28 0 0 1 16-22M46 12a28 28 0 0 1 16 22M22 62a28 28 0 0 0 28 0" stroke-dasharray="3 3"/>
</svg>
<div class="abs" style="left:181px;top:1854px"><div class="item-title">Collaboration</div><div class="item-text">Working together is the only way to maximize the team's potential</div></div>
<div class="abs sep" style="top:1939px"></div>

<svg class="abs" style="left:89px;top:1956px" width="72" height="70" viewBox="0 0 72 70" fill="none" stroke="#c1272d" stroke-width="2">
  <circle cx="30" cy="8" r="6"/><path d="M18 28a12 12 0 0 1 24 0"/>
  <circle cx="12" cy="46" r="5"/><path d="M2 66a10 10 0 0 1 20 0"/>
  <rect x="30" y="50" width="8" height="16"/><rect x="42" y="42" width="8" height="24"/><rect x="54" y="32" width="8" height="34"/>
  <path d="M10 34l18 8 34-20M56 20h7v7"/>
</svg>
<div class="abs" style="left:181px;top:1957px"><div class="item-title">Accountability</div><div class="item-text">Individual contributions are paramount to the team's success</div></div>
<div class="abs sep" style="top:2052px"></div>

<svg class="abs" style="left:89px;top:2066px" width="72" height="68" viewBox="0 0 72 68" fill="none" stroke="#c1272d" stroke-width="2">
  <rect x="6" y="8" width="22" height="14" rx="2"/><rect x="24" y="2" width="24" height="16" rx="2"/><rect x="44" y="8" width="22" height="14" rx="2"/>
  <path d="M30 8h12M30 12h12M10 14h12M50 14h12"/>
  <circle cx="14" cy="36" r="5"/><circle cx="36" cy="34" r="5"/><circle cx="58" cy="36" r="5"/>
  <path d="M4 66V52a10 10 0 0 1 20 0v14M26 66V50a10 10 0 0 1 20 0v16M48 66V52a10 10 0 0 1 20 0v14"/>
</svg>
<div class="abs" style="left:181px;top:2082px"><div class="item-title">Feedback</div><div class="item-text">Clear Feedback methods are in place</div></div>

<div class="abs svc-head" style="left:89px;top:2191px">Physics-Based Modeling and Hardware in the Loop</div>
<p class="abs" style="left:89px;top:2235px;width:440px;font-size:15.5px;line-height:24px">From data-driven system identification to real-time mathematical models for your simulation; we can handle that work for you. In addition, we are highly skilled on HIL testing and can support you in design and build phases to satisfy complex validation testing.</p>

<!-- Blog -->
<div class="abs post" style="top:1778px">
  <div class="pic" role="img" aria-label="Engineers discussing a design around a laptop" style="background:linear-gradient(160deg,#a9adb4,#d5d2cb 50%,#6b6f78)"></div>
  <div class="txt"><div class="meta">byPetra &nbsp;•&nbsp; January 2021</div><h4>What is the Design Process &nbsp;and Why is the System Broken?</h4><p>by R. Alvik, Helmstrand Plan Team Follow the "what", the "how",...</p></div>
</div>
<div class="abs post" style="top:1959px">
  <div class="pic" role="img" aria-label="Technician servicing a test rig" style="background:linear-gradient(170deg,#6f737b,#b1aea5 50%,#4a5068)"></div>
  <div class="txt"><div class="meta">byPetra &nbsp;•&nbsp; January 2021</div><h4>Process Series - The Good, the Bad and the Needed (1): Process and...</h4><p>*This is one in a series on the topic of Process in Product Development...</p></div>
</div>
<div class="abs post" style="top:2140px">
  <div class="pic" role="img" aria-label="Audience at a conference presentation" style="background:radial-gradient(circle at 50% 30%,#3d5a9c 0,#2a2b35 35%,#47474c 100%)"></div>
  <div class="txt"><div class="meta">byPetra &nbsp;•&nbsp; January 2021</div><h4>How Do I Get People to Really Listen When I Present a Solution?</h4><p>by M.T. Oberle, Helmstrand Plan Contributor *Follow the Series...</p></div>
</div>
<div class="abs view-all">VIEW ALL BLOGS</div>

<!-- Footer -->
<div class="abs footer"></div>
<div class="abs display" style="left:0;top:2540px;width:1200px;font-size:31px;line-height:1.1;color:#fff;text-align:center">Sign Up to Our Our Blog and News Letters and Receive the</div>
<div class="abs display" style="left:0;top:2590px;width:1200px;font-size:20px;color:#fff;text-align:center;font-weight:300">Latest Helmstrand Plan Updates!</div>
<div class="abs field"><svg width="16" height="12" viewBox="0 0 16 12"><rect width="16" height="12" rx="1" fill="#b5b5ba"/><path d="M0 1l8 6 8-6" fill="none" stroke="#fff" stroke-width="1.4"/></svg>Enter your email address</div>
<div class="abs subscribe">SUBSCRIBE</div>

<div class="abs f-brand"><span class="mark"></span>Darvik Systems</div>

<div class="abs f-icon" style="left:452px;top:2787px"><svg width="14" height="18" viewBox="0 0 14 18"><path d="M7 0a7 7 0 0 1 7 7c0 5-7 11-7 11S0 12 0 7a7 7 0 0 1 7-7z" fill="#fff"/><circle cx="7" cy="7" r="2.6" fill="#45434a"/></svg></div>
<div class="abs" style="left:505px;top:2780px"><div class="f-label">Address*</div><div class="f-text">North America Location: Larkfield, ON</div></div>

<div class="abs f-icon" style="left:823px;top:2787px"><svg width="16" height="12" viewBox="0 0 16 12"><rect width="16" height="12" rx="1" fill="#fff"/><path d="M0 1l8 6 8-6" fill="none" stroke="#45434a" stroke-width="1.4"/></svg></div>
<div class="abs" style="left:875px;top:2780px"><div class="f-label">Email*</div><div class="f-text">info@helmstrand-plan.example</div></div>

<div class="abs f-rule"></div>
<div class="abs copy">Darvik Systems © 2021 All Rights Reserved</div>
<div class="abs top-btn"><svg width="10" height="14" viewBox="0 0 10 14"><path d="M5 14V1M1 5l4-4 4 4" fill="none" stroke="#2a2a2e" stroke-width="1.3"/></svg></div>

</body>
</html>
```